business card design and letterhead for a building inspection company. We have a pre-purchase building and pest inspection ( i inspect house before people purchase it)
Updates

Tilda has been so so responsive and good, i highly recommend her

Industry/Entity Type

Building

Contact Information for Business Card

audience, solicitor, real estate agent, mortgage brokerthe rest of the info will be in the attachement business card

```html
<!DOCTYPE html>
<html lang="en">
<head>
<meta charset="utf-8">
<title>TrueNest Property Inspections – Business Card</title>
<link href="https://fonts.googleapis.com/css2?family=Open+Sans:ital,wght@0,400;0,600;0,700;1,400;1,700&display=swap" rel="stylesheet">
<style>
  :root{
    --brand-blue:#1d7ac4;
    --ink:#111111;
    --paper:#ffffff;
    --paper-shade:#f1f1f1;
    --backdrop:#dcdcdc;
    --muted:#5b6672;
  }
  *{box-sizing:border-box;margin:0;padding:0}
  html,body{width:1200px;height:901px;overflow:hidden}
  body{
    background:var(--backdrop);
    font-family:"Open Sans",Arial,sans-serif;
    display:flex;align-items:center;justify-content:center;gap:50px;
  }
  .card{
    position:relative;width:540px;height:310px;border-radius:26px;overflow:hidden;
    background:linear-gradient(160deg,var(--paper) 0%,var(--paper-shade) 100%);
    box-shadow:0 10px 26px rgba(0,0,0,.18);
  }
  .card__waves{position:absolute;inset:0;width:100%;height:100%}
  .wordmark{
    position:absolute;display:flex;flex-direction:column;align-items:flex-start;
  }
  .wordmark__name{
    display:flex;align-items:center;gap:8px;
    color:var(--brand-blue);font-weight:700;font-size:34px;letter-spacing:1px;line-height:1;
  }
  .wordmark__dot{width:14px;height:14px;border-radius:50%;background:var(--brand-blue)}
  .wordmark__sub{color:var(--brand-blue);font-weight:700;font-size:13px;letter-spacing:1.5px;margin-top:4px}
  .wordmark__tagline{color:var(--muted);font-size:10px;font-style:italic;margin-top:2px}
  .card--front .wordmark{left:190px;top:50px}
  .card--back .wordmark{left:150px;top:80px}
  .holder{position:absolute;left:26px;bottom:30px;color:var(--paper)}
  .holder__name{font-size:19px;font-weight:700;font-style:italic}
  .holder__role{font-size:13px;font-style:italic}
  .contacts{position:absolute;right:28px;bottom:20px;color:var(--paper);font-size:10.5px;list-style:none;text-align:right}
  .contacts li{display:flex;justify-content:flex-end;align-items:center;gap:6px;line-height:1.45;white-space:nowrap}
  .contacts svg{width:10px;height:10px;flex:none}
  .contacts__spacer{display:inline-block;width:10px;flex:none}
  .web{position:absolute;left:0;right:0;bottom:34px;text-align:center;color:var(--paper);font-size:13px;letter-spacing:3px}
</style>
</head>
<body>

<section class="card card--front" aria-label="Business card front">
  <svg class="card__waves" viewBox="0 0 540 310" preserveAspectRatio="none" aria-hidden="true">
    <path d="M0,165 C140,130 300,230 540,160 L540,310 L0,310Z" fill="var(--brand-blue)"/>
    <path d="M0,151 C140,114 300,216 540,147" fill="none" stroke="var(--ink)" stroke-width="8"/>
    <path d="M0,140 C140,104 300,204 540,137" fill="none" stroke="var(--ink)" stroke-width="2.5"/>
    <path d="M0,0 L120,0 C80,40 60,100 0,138Z" fill="var(--brand-blue)"/>
    <path d="M128,0 C88,44 66,104 0,146" fill="none" stroke="var(--ink)" stroke-width="6"/>
  </svg>
  <div class="wordmark">
    <div class="wordmark__name"><span class="wordmark__dot"></span>TRUENEST</div>
    <div class="wordmark__sub">PROPERTY INSPECTIONS</div>
    <div class="wordmark__tagline">Building and pest reports</div>
  </div>
  <div class="holder">
    <div class="holder__name">Sarah Tilda</div>
    <div class="holder__role">Owner / CEO</div>
  </div>
  <ul class="contacts">
    <li>Suite 14, Harbour Ct <svg viewBox="0 0 10 10"><path d="M5 0a3.5 3.5 0 0 0-3.5 3.5C1.5 6 5 10 5 10s3.5-4 3.5-6.5A3.5 3.5 0 0 0 5 0z" fill="#fff"/></svg></li>
    <li>27 Lane Rd 4021 <span class="contacts__spacer"></span></li>
    <li>0412 558 301 <svg viewBox="0 0 10 10"><circle cx="5" cy="5" r="5" fill="#fff"/></svg></li>
    <li>0733 904 112 <svg viewBox="0 0 10 10"><circle cx="5" cy="5" r="5" fill="#fff"/></svg></li>
    <li>hello@truenestinspect.com <svg viewBox="0 0 10 10"><circle cx="5" cy="5" r="5" fill="#fff"/></svg></li>
    <li>www.truenestinspect.com <svg viewBox="0 0 10 10"><circle cx="5" cy="5" r="5" fill="#fff"/></svg></li>
  </ul>
</section>

<section class="card card--back" aria-label="Business card back">
  <svg class="card__waves" viewBox="0 0 540 310" preserveAspectRatio="none" aria-hidden="true">
    <path d="M0,0 L150,0 C90,60 60,140 0,170Z" fill="var(--brand-blue)"/>
    <path d="M0,230 C160,200 330,290 540,220 L540,310 L0,310Z" fill="var(--brand-blue)"/>
    <path d="M0,218 C160,186 330,276 540,206" fill="none" stroke="var(--ink)" stroke-width="8"/>
    <path d="M0,206 C160,176 330,262 540,196" fill="none" stroke="var(--ink)" stroke-width="2.5"/>
  </svg>
  <div class="wordmark">
    <div class="wordmark__name"><span class="wordmark__dot"></span>TRUENEST</div>
    <div class="wordmark__sub">PROPERTY INSPECTIONS</div>
    <div class="wordmark__tagline">Building and pest reports</div>
  </div>
  <div class="web">www.truenestinspect.com</div>
</section>

</body>
</html>
```